Professional/modern business card design for construction company

We need a new business card design, double sided keeping it modern, sleek, professional and simple. We are an earthmoving business but do not want any pictures of machinery. I would like one side to have the logo and the other to have all the information, keeping with the colors in our logo. The business card will need to be able to be customised so we can use it for several different managers., we would also like to be able to use the design to apply it to other stationary ie. letterheads, notebooks etc. We do not really have a tag line but we could put on there that we specialise in - Agriculture, Civil Construction and Mining.

Contact Information for Business Card

Brolga Ridge Excavations Pty Ltd
ABN 58 402 937 615
82 Gumleaf Creek Road, Moree NSW 2400

Harold Benton
Managing Director
P 0418 639 204
E haroldbenton@brolgaridgeexc.com.au

Font styles to use
Serif
Sans Serif

Requirements
Nice to have
• I have attached some examples of ideas.
Should not have
• images of machinery

```html
<!DOCTYPE html>
<html lang="en">
<head>
<meta charset="utf-8">
<title>Brolga Ridge Excavations – Business Card</title>
<link rel="stylesheet" href="https://fonts.googleapis.com/css2?family=Montserrat:wght@400;500;700;800&display=swap">
<style>
  :root {
    --orange: #f7931e;
    --charcoal: #3b3b3b;
    --charcoal-deep: #333333;
    --slate: #4a4a4a;
    --grey-light: #c9c9c9;
    --grey-mid: #9d9d9d;
    --paper: #ffffff;
    --backdrop: #e6e6e8;
    --ink: #2f2f2f;
  }
  html, body {
    margin: 0;
    padding: 0;
    width: 1200px;
    height: 800px;
    overflow: hidden;
    background: var(--backdrop);
    font-family: "Montserrat", Arial, sans-serif;
  }
  .stage {
    position: relative;
    width: 1200px;
    height: 800px;
    display: flex;
    align-items: center;
    justify-content: center;
    gap: 50px;
  }
  .card {
    width: 525px;
    height: 300px;
    display: block;
    box-shadow: 0 10px 28px rgba(0,0,0,0.16);
  }
  .card-front .surface { fill: var(--charcoal); }
  .band { fill: var(--orange); }
  .brand-name { font-family: "Montserrat", Arial, sans-serif; font-weight: 800; letter-spacing: 0.5px; }
  .card-front .brand-name { fill: var(--paper); }
  .card-back .brand-name { fill: var(--ink); }
  .brand-mark { fill: var(--orange); }
  .card-back .surface { fill: var(--paper); }
  .edge-bar { fill: var(--orange); }
  .facet-dark { fill: var(--slate); }
  .facet-light { fill: var(--grey-light); }
  .facet-orange { fill: var(--orange); }
  .icon-disc { fill: var(--orange); }
  .icon-glyph { fill: none; stroke: var(--charcoal-deep); stroke-width: 1.6; stroke-linecap: round; stroke-linejoin: round; }
  .contact-line { font-family: "Montserrat", Arial, sans-serif; font-size: 9px; font-weight: 500; fill: var(--ink); }
  .role-title { font-family: "Montserrat", Arial, sans-serif; font-size: 9px; font-weight: 400; fill: var(--paper); }
  .person-name { font-family: "Montserrat", Arial, sans-serif; font-size: 15px; font-weight: 700; fill: var(--paper); }
</style>
</head>
<body>
<main class="stage">

  <!-- Logo side -->
  <svg class="card card-front" viewBox="0 0 525 300" xmlns="http://www.w3.org/2000/svg">
    <rect class="surface" width="525" height="300"/>
    <polygon class="band band-upper" points="345,58 525,58 525,92 395,92"/>
    <polygon class="band band-lower" points="0,168 165,168 225,200 0,200"/>
    <rect class="brand-mark" x="130" y="112" width="14" height="14"/>
    <text class="brand-name" x="154" y="124" font-size="17">BROLGA RIDGE</text>
    <text class="brand-name" x="154" y="143" font-size="11">EXCAVATIONS PTY LTD</text>
  </svg>

  <!-- Information side -->
  <svg class="card card-back" viewBox="0 0 525 300" xmlns="http://www.w3.org/2000/svg">
    <rect class="surface" width="525" height="300"/>
    <rect class="edge-bar" x="0" y="0" width="16" height="300"/>

    <rect class="brand-mark" x="40" y="30" width="12" height="12"/>
    <text class="brand-name" x="60" y="41" font-size="15">BROLGA RIDGE</text>
    <text class="brand-name" x="60" y="56" font-size="9.5">EXCAVATIONS PTY LTD</text>

    <polygon class="facet-light" points="420,92 445,60 525,200 330,300 300,300"/>
    <polygon class="facet-dark" points="445,60 525,60 525,200"/>
    <polygon class="facet-orange" points="230,300 525,150 525,300"/>

    <g class="contact contact-address">
      <circle class="icon-disc" cx="48" cy="102" r="10"/>
      <path class="icon-glyph" d="M48 108 C44 103 43.5 101 43.5 99.5 A4.5 4.5 0 0 1 52.5 99.5 C52.5 101 52 103 48 108 Z"/>
      <circle class="icon-glyph" cx="48" cy="99.5" r="1.4"/>
      <text class="contact-line" x="66" y="99">ABN 58 402 937 615</text>
      <text class="contact-line" x="66" y="111">82 Gumleaf Creek Road, Moree NSW 2400</text>
    </g>
    <g class="contact contact-phone">
      <circle class="icon-disc" cx="48" cy="135" r="10"/>
      <path class="icon-glyph" d="M44.5 130.5 l2 -0.5 l1.5 3 l-1.3 1.2 a7 7 0 0 0 3.2 3.2 l1.2 -1.3 l3 1.5 l-0.5 2 a2 2 0 0 1 -2 1.2 a10 10 0 0 1 -8.3 -8.3 a2 2 0 0 1 1.2 -2 z"/>
      <text class="contact-line" x="66" y="138">P 0418 639 204</text>
    </g>
    <g class="contact contact-email">
      <circle class="icon-disc" cx="48" cy="168" r="10"/>
      <rect class="icon-glyph" x="42.5" y="164" width="11" height="8" rx="1"/>
      <path class="icon-glyph" d="M42.8 164.5 L48 168.5 L53.2 164.5"/>
      <text class="contact-line" x="66" y="171">E haroldbenton@brolgaridgeexc.com.au</text>
    </g>

    <text class="role-title" x="320" y="279">Managing Director</text>
    <text class="person-name" x="408" y="280">Harold Benton</text>
  </svg>

</main>
</body>
</html>
```